Beauty Page

**UPDATED Brief**
We are looking for a website for a beauty organisation that targets both MEN & WOMAN. The focus of the company is in four main areas:

- Health
* Naturopathy & Remedial Massage
- Body
* Yoga
* Personal Training
* Massage
- Skin
* Skin care products such as Velquessa
- Beauty
* Waxing
* Eye Treatments

We have attached the logo, (a sample of the website that I did - based on the book) and the sample of the pdf book
Updates

Dear All,

Thank you for your patience regarding the beauty contest. We were not happy with the designs that were submitted to us. We therefore had the Graphic designer to do the pricelist book to get all the colours for the organisation.

We are now happy to relaunch the contest and invite you all to take a look at the brief, download a sample of the book and the website we designed on what I’m looking for (the website is only a draft so I don’t want you to copy it) and let your creative mind go wild and present some suggestions to us.

Thanks

 

Target Market(s)

Woman & Men age 24 - 60

Industry/Entity Type

It Company

Requirements
Must have
• Use of main colours
Black
White
Gray - (CYMK - 65, 58, 57, 37)
Purpleish - Maroon (CYMK - 52, 69, 47, 25)

Use of the three color dots on the page.
(white, maroon & Gray)
Same fonts as the book
- Helvetica LT Std
Should not have
• Logo must not be altered i.e different colours, fonts, shadows etc...

```html
<!DOCTYPE html>
<html lang="en">
<head>
<meta charset="utf-8">
<title>Lumora – Health, Body and Skin Care Centre</title>
<link href="https://fonts.googleapis.com/css2?family=Arimo:wght@400;700&display=swap" rel="stylesheet">
<style>
  :root {
    --black: #0d0d0d;
    --white: #ffffff;
    --gray: #4b4b4d;
    --gray-mid: #6b6b6b;
    --gray-light: #bdbdbd;
    --maroon: #6b2f4a;
    --maroon-dark: #4f2035;
    --maroon-light: #8a4b67;
    --text: #4a4a4a;
    --page-bg-top: #0e0e0e;
    --page-bg-bottom: #4d4d4d;
  }
  * { box-sizing: border-box; margin: 0; padding: 0; }
  html, body { width: 973px; height: 1200px; overflow: hidden; }
  body {
    position: relative;
    font-family: "Arimo", Helvetica, Arial, sans-serif;
    background: linear-gradient(to bottom, var(--page-bg-top), var(--page-bg-bottom));
    color: var(--text);
  }
  .abs { position: absolute; }

  /* Header */
  .site-header {
    left: 58px; top: 28px; width: 860px; height: 158px;
    background: var(--white); border-radius: 14px;
  }
  .brand-name {
    left: 37px; top: 22px; font-size: 96px; font-weight: 700;
    color: var(--black); letter-spacing: -2px; line-height: 1;
  }
  .brand-tagline {
    left: 38px; top: 114px; font-size: 25px; color: var(--black); line-height: 1;
  }
  .search {
    left: 610px; top: 35px; width: 212px; height: 38px;
    border-radius: 4px; overflow: hidden; display: flex;
    box-shadow: 0 1px 3px rgba(0,0,0,.3);
  }
  .search-field {
    flex: 1; background: linear-gradient(#fafafa, #d6d6d6);
    color: #8a8a8a; font-size: 14px; padding: 12px 0 0 28px;
  }
  .search-go {
    width: 40px; background: var(--maroon); color: var(--white);
    font-size: 11px; font-weight: 700; text-align: center; padding-top: 13px;
  }
  .phone { left: 675px; top: 100px; display: flex; align-items: center; gap: 9px; }
  .phone-icon {
    width: 30px; height: 32px; border-radius: 6px; background: var(--maroon);
    display: flex; align-items: center; justify-content: center;
  }
  .phone-number { font-size: 24px; font-weight: 700; color: var(--maroon); }

  /* Navigation */
  .main-nav {
    left: 58px; top: 194px; width: 860px; height: 41px; border-radius: 10px 10px 0 0;
    background: linear-gradient(#3a3a3a, #0a0a0a 55%, #1a1a1a);
  }
  .nav-item {
    position: absolute; top: 12px; color: var(--white);
    font-size: 14px; font-weight: 700; letter-spacing: .1px;
  }
  .nav-item.is-active {
    top: 2px; height: 37px; padding: 10px 11px 0; background: #111;
    border-radius: 4px 4px 0 0; box-shadow: inset 0 1px 0 #444;
  }
  .submenu {
    left: 357px; top: 236px; width: 164px; height: 82px; background: var(--black);
    z-index: 5; padding: 7px 0 0 16px;
  }
  .submenu li { list-style: none; color: var(--white); font-size: 14px; line-height: 23.5px; }

  /* Main panel */
  .main-panel {
    left: 58px; top: 242px; width: 860px; height: 866px; border-radius: 14px;
    background: linear-gradient(#ffffff, #f2eef1); overflow: hidden;
  }
  .hero-photo {
    right: 0; top: 0; width: 330px; height: 350px;
    background: radial-gradient(circle at 60% 40%, #f3d3bd, #e9b896 40%, #f7ece6 80%);
  }
  .hero-heading {
    left: 77px; top: 86px; font-size: 29px; font-weight: 700;
    color: var(--gray-mid); line-height: 35px;
  }
  .btn {
    position: absolute; color: var(--white); font-weight: 700; font-size: 14px;
    text-align: center; border-radius: 4px;
    background: linear-gradient(var(--maroon-light), var(--maroon) 50%, var(--maroon-dark));
    box-shadow: 0 2px 4px rgba(0,0,0,.35);
  }
  .hero-btn { left: 308px; top: 202px; width: 152px; height: 46px; line-height: 46px; }
  .hero-wave { left: 0; top: 280px; width: 860px; height: 110px; }
  .slider-dots { left: 684px; top: 314px; display: flex; gap: 5px; }
  .dot { width: 22px; height: 22px; border-radius: 50%; }
  .dot.white { background: var(--white); border: 2px solid #222; }
  .dot.maroon { background: var(--maroon); }
  .dot.gray { background: var(--gray); }

  .slider-arrow {
    width: 42px; height: 58px; background: radial-gradient(circle at 50% 40%, #3a3a3a, #000);
    z-index: 4; display: flex; align-items: center;
  }
  .slider-arrow.prev { left: 58px; top: 393px; border-radius: 0 30px 30px 0; justify-content: flex-end; padding-right: 12px; }
  .slider-arrow.next { left: 877px; top: 393px; border-radius: 30px 0 0 30px; padding-left: 12px; }
  .arrow-disc {
    width: 22px; height: 22px; border-radius: 50%; background: linear-gradient(#fff, #ccc);
    display: flex; align-items: center; justify-content: center;
  }

  /* Side boxes */
  .side-box { left: 80px; width: 265px; border-radius: 4px; }
  .newsletter { top: 607px; height: 191px; background: var(--maroon); }
  .box-tab {
    position: absolute; left: 69px; width: 286px; height: 50px; border-radius: 8px;
    color: var(--white); font-size: 14px; font-weight: 700; z-index: 2;
    box-shadow: 0 3px 5px rgba(0,0,0,.4);
  }
  .newsletter-tab { top: 617px; background: linear-gradient(var(--maroon-light), var(--maroon-dark)); text-align: center; line-height: 34px; }
  .newsletter-field { left: 113px; top: 666px; width: 194px; height: 36px; background: var(--maroon-light); opacity: .8; }
  .subscribe-btn { left: 115px; top: 719px; width: 154px; height: 47px; line-height: 47px; border: 1px solid var(--maroon-dark); }

  .products { top: 822px; height: 260px; background: var(--black); }
  .products-tab { top: 822px; height: 58px; background: linear-gradient(#5a5a5a, #1a1a1a 60%, #000); padding: 18px 0 0 51px; }
  .products-photo {
    left: 103px; top: 876px; width: 219px; height: 164px;
    background: linear-gradient(160deg, #f5f7ee, #cfe1a6 55%, #9fbf63);
  }
  .products-caption { left: 119px; top: 1001px; font-size: 13px; font-weight: 700; color: #111; line-height: 15px; }
  .products-btn { left: 134px; top: 1042px; width: 153px; height: 36px; line-height: 36px; }

  /* Welcome */
  .section-title { position: absolute; color: var(--gray-mid); font-weight: 700; }
  .section-title strong { color: var(--maroon-dark); }
  .welcome-title { left: 393px; top: 655px; font-size: 22px; }
  .dotted { position: absolute; border-top: 2px dotted var(--maroon); }
  .welcome-photo {
    left: 397px; top: 690px; width: 160px; height: 147px;
    background: linear-gradient(#f6f2ee, #f0dccb 50%, #f6f2ee);
  }
  .welcome-text { left: 568px; top: 716px; width: 330px; font-size: 11.5px; font-weight: 700; line-height: 23.5px; color: var(--text); }
  .view-more { left: 574px; top: 821px; font-size: 11px; font-weight: 700; color: var(--maroon); }

  .events-title { left: 410px; top: 879px; font-size: 18px; }
  .event-card {
    position: absolute; top: 921px; width: 224px; height: 139px;
    border: 1px solid #bbb; border-radius: 5px; overflow: hidden;
    background: linear-gradient(#fff, #e6e6e6);
  }
  .event-photo { position: absolute; top: 0; height: 100%; width: 120px; }
  .event-card h3 { position: absolute; font-size: 12px; font-weight: 400; color: #111; }
  .event-card p { position: absolute; font-size: 11.5px; color: #8a8a8a; line-height: 17px; }
  .event-card .more { position: absolute; font-size: 12px; color: #333; }

  /* Footer */
  .social { top: 1134px; width: 32px; height: 32px; border-radius: 50%; background: #d9d9d9; border: 2px solid #999; }
  .footer-links { left: 518px; top: 1126px; font-size: 12px; color: var(--white); word-spacing: 2px; }
  .footer-links span { margin: 0 13px; }
  .copyright { left: 524px; top: 1160px; font-size: 12px; color: #d0d0d0; }
</style>
</head>
<body>

<header class="abs site-header">
  <div class="abs brand-name">LUMORA</div>
  <div class="abs brand-tagline">Health, Body and Skin Care Centre</div>
  <div class="abs search">
    <div class="search-field">Search</div>
    <div class="search-go">GO</div>
  </div>
  <div class="abs phone">
    <div class="phone-icon">
      <svg width="14" height="20" viewBox="0 0 14 20"><path d="M4 1 L7 5 L5 7 C5.5 10 7 12.5 9 14 L11 12 L13 16 L11 18.5 C6 18 1 11 2 3 Z" fill="none" stroke="#fff" stroke-width="1.4" stroke-linejoin="round"/></svg>
    </div>
    <div class="phone-number">9471 3620</div>
  </div>
</header>

<nav class="abs main-nav">
  <span class="nav-item" style="left:33px">HOME</span>
  <span class="nav-item" style="left:111px">ABOUT US</span>
  <span class="nav-item" style="left:215px">HEALTH</span>
  <span class="nav-item is-active" style="left:289px">BODY</span>
  <span class="nav-item" style="left:373px">SKIN</span>
  <span class="nav-item" style="left:440px">BEAUTY</span>
  <span class="nav-item" style="left:531px">GENERAL INFORMATION</span>
  <span class="nav-item" style="left:729px">CONTACT US</span>
</nav>
<ul class="abs submenu">
  <li>Yoga</li>
  <li>Personal Training</li>
  <li>Massage</li>
</ul>

<main class="abs main-panel">
  <div class="abs hero-photo" role="img" aria-label="Woman in a white towel smelling red flowers above water"></div>
  <h1 class="abs hero-heading">Encompassing<br>the whole body to create<br>a healthier you</h1>
  <div class="btn hero-btn">FIND OUT MORE</div>
  <svg class="abs hero-wave" viewBox="0 0 860 110" preserveAspectRatio="none">
    <path d="M0 25 C200 -10 420 20 600 40 C720 52 800 45 860 30 L860 58 C780 75 690 80 560 70 C380 55 180 30 0 50 Z" fill="#0d0d0d"/>
    <path d="M0 50 C180 30 380 55 560 70 C690 80 780 75 860 58 L860 80 C780 96 680 100 540 90 C360 76 170 60 0 72 Z" fill="#ffffff"/>
    <path d="M0 72 C170 60 360 76 540 90 C680 100 780 96 860 80 L860 110 L0 110 Z" fill="#4b4b4d"/>
    <path d="M0 84 C170 74 360 90 540 104 C680 112 780 108 860 94 L860 110 L0 110 Z" fill="#f8f5f7"/>
  </svg>
  <div class="abs slider-dots">
    <span class="dot white"></span><span class="dot maroon"></span><span class="dot gray"></span>
  </div>
</main>

<div class="abs slider-arrow prev"><span class="arrow-disc"><svg width="8" height="10" viewBox="0 0 8 10"><path d="M2 1 L6 5 L2 9" fill="none" stroke="#222" stroke-width="1.6"/></svg></span></div>
<div class="abs slider-arrow next"><span class="arrow-disc"><svg width="8" height="10" viewBox="0 0 8 10"><path d="M6 1 L2 5 L6 9" fill="none" stroke="#222" stroke-width="1.6"/></svg></span></div>

<section>
  <div class="abs side-box newsletter"></div>
  <div class="box-tab newsletter-tab">NEWSLETTER</div>
  <div class="abs newsletter-field"></div>
  <div class="btn subscribe-btn">SUBSCRIBE</div>
</section>

<section>
  <div class="abs side-box products"></div>
  <div class="box-tab products-tab">PRODUCT &amp; SERVICES</div>
  <div class="abs products-photo" role="img" aria-label="Smiling mature couple outdoors"></div>
  <div class="abs products-caption">Check out our range from<br>LUMORA</div>
  <div class="btn products-btn">FIND OUT MORE</div>
</section>

<section>
  <h2 class="section-title welcome-title">Welcome to <strong>LUMORA</strong></h2>
  <div class="dotted" style="left:397px;top:683px;width:257px"></div>
  <div class="abs welcome-photo" role="img" aria-label="Woman eating a fruit salad"></div>
  <p class="abs welcome-text">Maintaining a healthy body and mind is of the highest importance. Lumora's highly qualified and experienced therapists will provide you withthe optimum in natural health services and products</p>
  <div class="abs view-more">VIEW MORE</div>

  <h2 class="section-title events-title">SPECIAL <strong>EVENTS</strong></h2>
  <div class="dotted" style="left:408px;top:905px;width:186px"></div>

  <article class="event-card" style="left:403px">
    <div class="event-photo" style="left:0;background:linear-gradient(90deg,#d9a47e,#f0d2bb 70%,rgba(255,255,255,0))" role="img" aria-label="Woman receiving a back massage"></div>
    <h3 style="left:89px;top:15px">Lorem ipsum dolor sit</h3>
    <p style="left:94px;top:45px">Lorem ipsum dolor sit<br>amet,consectetuer<br>adipiscing elit.</p>
    <span class="more" style="left:142px;top:103px">View more</span>
  </article>

  <article class="event-card" style="left:667px">
    <div class="event-photo" style="right:0;width:110px;background:linear-gradient(270deg,#e2b08f,#f2d6c3 70%,rgba(255,255,255,0))" role="img" aria-label="Woman with smooth skin touching her shoulder"></div>
    <h3 style="left:10px;top:13px">Lorem ipsum dolor sit</h3>
    <p style="left:11px;top:43px">Lorem ipsum dolor sit<br>amet,consectetuer<br>adipiscing elit.</p>
    <span class="more" style="left:16px;top:107px">View more</span>
  </article>
</section>

<footer>
  <span class="abs social" style="left:96px" aria-label="Social link"></span>
  <span class="abs social" style="left:146px" aria-label="Social link"></span>
  <span class="abs social" style="left:197px" aria-label="News feed link"></span>
  <div class="abs footer-links">Terms &amp; Conditions<span>|</span>Privacy<span>|</span>Contact us</div>
  <div class="abs copyright">Copyright © 2011, LUMORA, All Rights Reserved</div>
</footer>

</body>
</html>
```